Mortgage Broking boutique Business

I’m wanting a revamped look to my existing business card design. I do like the black and silver but happy to have other colours introduced based on your creation. I’ve attached a copy of my current card so you can have a starting point updated details noted brloe. I deal with high net worth individuals so need my card to be sophisticated, classy that gives off a classy vibe

Target Market(s)

High net worth, wealthy

Industry/Entity Type

Mortgage Brokerage

Contact Information for Business Card

Job title: Finance Executive
Phone: +61 7 3287 4419
Mobile: 0471 352 608
Email: marcus@quillbrookcapital.com.au
Web: www.quillbrookcapital.com.au
Address: level 36 Tindale Court, 58 Harwick St Brisbane QLD 4000

Font styles to use
Other font styles liked:
• Helvetica

Colors

Designer to choose colors to be used in the design.

Requirements
Must have
• Use my existing card design as a starting point

```html
<!DOCTYPE html>
<html lang="en">
<head>
<meta charset="utf-8">
<title>Quillbrook Capital – Business Card</title>
<link href="https://fonts.googleapis.com/css2?family=Jost:wght@500&family=Source+Sans+3:wght@400&family=PT+Sans+Narrow&display=swap" rel="stylesheet">
<style>
  :root {
    --ink: #111214;
    --card-dark: #1b1f25;
    --card-mid: #262d36;
    --pearl: #dcdcdc;
    --silver-light: #f2f4f5;
    --silver-dark: #6d6f72;
    --page: #ffffff;
  }
  * { margin: 0; padding: 0; box-sizing: border-box; }
  html, body {
    width: 877px; height: 1200px; overflow: hidden;
    background: var(--page);
  }
  .sheet { position: relative; width: 877px; height: 1200px; }
  .card { position: absolute; left: 0; width: 877px; overflow: hidden; }
  .card--front { top: 0; height: 570px; }
  .card--back { top: 629px; height: 571px; }
  .card svg { position: absolute; inset: 0; }

  .brand {
    position: absolute; left: 0; width: 877px; text-align: center;
    font-family: "Jost", "Futura", sans-serif; font-weight: 500; color: var(--ink);
  }
  .brand__name { top: 226px; font-size: 82px; letter-spacing: 7px; line-height: 1; }
  .brand__sub { top: 328px; font-size: 49px; letter-spacing: 6px; line-height: 1; }

  .job-title {
    position: absolute; left: 166px; top: 114px;
    font-family: "PT Sans Narrow", "Arial Narrow", sans-serif;
    font-size: 60px; color: var(--ink); line-height: 1; letter-spacing: -0.5px;
  }
  .rule {
    position: absolute; left: 170px; top: 206px; width: 354px; height: 3px;
    background: var(--ink);
  }
  .contact {
    position: absolute; left: 166px; width: 360px;
    font-family: "Source Sans 3", "Helvetica", sans-serif;
    font-size: 19px; color: var(--ink); line-height: 25px;
  }
  .contact__icon { position: absolute; left: 0; }
  .contact__text { position: absolute; left: 50px; white-space: nowrap; }
  .contact--address { top: 246px; }
  .contact--address .contact__text { text-align: center; }
  .contact--phone { top: 322px; }
  .contact--email { top: 385px; }
  .contact--web { top: 445px; }
</style>
</head>
<body>
<div class="sheet">

  <section class="card card--front">
    <svg width="877" height="570" viewBox="0 0 877 570">
      <defs>
        <linearGradient id="frontBg" x1="0" x2="1" y1="0" y2="0">
          <stop offset="0" stop-color="#111316"/>
          <stop offset="0.3" stop-color="var(--card-mid)"/>
          <stop offset="0.55" stop-color="#15181c"/>
          <stop offset="0.8" stop-color="var(--card-mid)"/>
          <stop offset="1" stop-color="#121418"/>
        </linearGradient>
        <linearGradient id="frontRim" x1="0" x2="1" y1="0" y2="0">
          <stop offset="0" stop-color="var(--silver-light)"/>
          <stop offset="0.35" stop-color="var(--silver-dark)"/>
          <stop offset="0.55" stop-color="var(--silver-light)"/>
          <stop offset="0.75" stop-color="var(--silver-dark)"/>
          <stop offset="1" stop-color="var(--silver-light)"/>
        </linearGradient>
      </defs>
      <rect class="card__ground" width="877" height="570" fill="url(#frontBg)"/>
      <ellipse class="card__rim" cx="438" cy="285" rx="606" ry="215" fill="url(#frontRim)"/>
      <ellipse class="card__panel" cx="438" cy="285" rx="600" ry="207" fill="var(--pearl)"/>
    </svg>
    <div class="brand brand__name">QUILLBROOK</div>
    <div class="brand brand__sub">CAPITAL</div>
  </section>

  <section class="card card--back">
    <svg width="877" height="571" viewBox="0 0 877 571">
      <defs>
        <linearGradient id="backBg" x1="0" x2="1" y1="0" y2="0">
          <stop offset="0" stop-color="var(--card-mid)"/>
          <stop offset="0.5" stop-color="#15181c"/>
          <stop offset="1" stop-color="var(--card-mid)"/>
        </linearGradient>
        <linearGradient id="backRim" x1="0" x2="0" y1="0" y2="1">
          <stop offset="0" stop-color="var(--silver-light)"/>
          <stop offset="0.4" stop-color="var(--silver-dark)"/>
          <stop offset="0.7" stop-color="var(--silver-light)"/>
          <stop offset="1" stop-color="var(--silver-dark)"/>
        </linearGradient>
      </defs>
      <rect class="card__ground" width="877" height="571" fill="url(#backBg)"/>
      <circle class="card__rim" cx="440" cy="285" r="381" fill="url(#backRim)"/>
      <circle class="card__panel" cx="440" cy="285" r="375" fill="var(--pearl)"/>
    </svg>

    <div class="job-title">Finance Executive</div>
    <div class="rule"></div>

    <div class="contact contact--address">
      <svg class="contact__icon" width="20" height="34" viewBox="0 0 20 34" aria-hidden="true">
        <path d="M10 0a10 10 0 0 0-10 10c0 8 10 24 10 24s10-16 10-24A10 10 0 0 0 10 0zm0 14a4 4 0 1 1 0-8 4 4 0 0 1 0 8z" fill="var(--ink)"/>
      </svg>
      <div class="contact__text">level 36 Tindale Court, 58 Harwick<br>St Brisbane QLD 4000</div>
    </div>

    <div class="contact contact--phone">
      <svg class="contact__icon" width="20" height="34" viewBox="0 0 20 34" aria-hidden="true">
        <rect x="1" y="1" width="18" height="32" rx="3" fill="none" stroke="var(--ink)" stroke-width="2"/>
        <rect x="4" y="5" width="12" height="21" fill="var(--ink)"/>
        <circle cx="10" cy="29.5" r="1.6" fill="var(--ink)"/>
      </svg>
      <div class="contact__text" style="top:5px">+61 7 3287 4419</div>
    </div>

    <div class="contact contact--email">
      <svg class="contact__icon" width="24" height="20" viewBox="0 0 24 20" aria-hidden="true">
        <path d="M1 8 12 1l11 7v11H1z" fill="none" stroke="var(--ink)" stroke-width="2"/>
        <path d="M1 8l11 7 11-7L12 1z" fill="var(--ink)"/>
      </svg>
      <div class="contact__text" style="top:-2px">marcus@quillbrookcapital.com.au</div>
    </div>

    <div class="contact contact--web">
      <svg class="contact__icon" width="24" height="24" viewBox="0 0 24 24" aria-hidden="true">
        <circle cx="12" cy="12" r="11" fill="var(--ink)"/>
        <g fill="none" stroke="var(--pearl)" stroke-width="1.3">
          <ellipse cx="12" cy="12" rx="5" ry="11"/>
          <line x1="12" y1="1" x2="12" y2="23"/>
          <line x1="1" y1="12" x2="23" y2="12"/>
          <line x1="3" y1="6.5" x2="21" y2="6.5"/>
          <line x1="3" y1="17.5" x2="21" y2="17.5"/>
        </g>
      </svg>
      <div class="contact__text" style="top:-1px">www.quillbrookcapital.com.au</div>
    </div>
  </section>

</div>
</body>
</html>
```